Children's Theater Production (Lanterns in Barrowmere)

I run LFDW, the Little Footlights Drama Workshop, a theater dedicated to bringing kids to the performing arts, both in the audience and as performers. Currently we're rehearsing Lanterns in Barrowmere, a Farrowby comedy (adapted for young audiences) about two sets of twins and mistaken identity. I need a poster to market that show to the community. I'll be making paper copies and will ideally have something I can put on our website, as well.
I'm looking for something that appeals to families with kids (though not too childish; many of our group are teens), something that reflects the story (and/or Farrowby), I'd like it to communicate FUN and FUNNY. Offbeat is great. Our patrons are generally well educated, fairly theater savvy moms and dads who are coming to see their sons and daughters on stage, or just love to bring their kids to the theater. But this is likely the first Farrowby many of them will be attending, so I'd love the poster to also communicate "approachable;" some people still struggle with Farrowby-phobia :-)
The other details necessary to include on the poster are as follows, and *I'm not married to the exact verbiage I've got here*:
Little Footlights Drama Workshop (LFDW) (logo will follow)
Lanterns in Barrowmere
by Edmund Farrowby
adapted by Dennis Paulwick
Performances located at
482 N. Larkmoor Avenue, Shepherdstown, WV
All tickets are general admission, $8
Performances are June 8 through 17, 2012 ~ Fridays at 7:00 p.m., Saturdays and Sundays at 2:00 p.m.
Sign interpreted performance on Friday, June 15, 2012
Purchase tickets online at MyLFDW.com, or call 304-555-0187 for more information.

```html
<!DOCTYPE html>
<html lang="en">
<head>
<meta charset="utf-8">
<title>Lanterns in Barrowmere — Little Footlights Drama Workshop</title>
<link rel="stylesheet" href="https://fonts.googleapis.com/css2?family=Delius&family=Philosopher:wght@700&family=Marcellus&display=swap">
<style>
  :root {
    --sun: #ffd400;
    --sun-deep: #f7c300;
    --sun-soft: #ffdf3a;
    --ink: #2a2216;
    --brand-blue: #1f6fa8;
    --rule-blue: #1d5f9f;
    --burst-red: #e3170d;
  }
  * { box-sizing: border-box; margin: 0; padding: 0; }
  html, body { width: 800px; height: 1200px; overflow: hidden; }
  body { font-family: "Delius", "Trebuchet MS", sans-serif; color: var(--ink); }

  .poster {
    position: relative;
    width: 800px;
    height: 1200px;
    overflow: hidden;
    background: var(--sun);
  }
  .backdrop-pattern {
    position: absolute;
    inset: 0;
    background: radial-gradient(circle at 60% 45%, var(--sun-soft) 0%, var(--sun) 55%, var(--sun-deep) 100%);
  }

  .line { position: absolute; left: 0; width: 800px; text-align: center; white-space: nowrap; }

  .brand {
    position: absolute;
    left: 90px; top: 30px;
    width: 620px; height: 300px;
    display: flex;
    align-items: center;
    gap: 28px;
    color: var(--brand-blue);
    font-family: "Delius", "Trebuchet MS", sans-serif;
  }
  .brand-dot {
    flex: 0 0 150px; height: 150px;
    border-radius: 50%;
    background: var(--brand-blue);
  }
  .brand-name { line-height: 1; }
  .brand-initials { display: block; font-size: 140px; letter-spacing: 4px; }
  .brand-full { display: block; font-size: 29px; margin-top: 14px; letter-spacing: 1px; }

  .presents { top: 350px; font-size: 24px; }
  .title {
    top: 380px;
    font-family: "Philosopher", "Georgia", serif;
    font-weight: 700;
    font-size: 56px;
    text-shadow: 3px 4px 6px rgba(80, 60, 0, 0.45);
  }
  .author { top: 470px; font-size: 28px; }
  .adapter { top: 508px; font-size: 21px; }
  .dates { top: 550px; font-size: 50px; }
  .venue { top: 607px; font-size: 25px; }

  .admission {
    position: absolute;
    top: 648px; left: 0; width: 800px;
    display: flex; justify-content: center; align-items: baseline; gap: 20px;
  }
  .admission-label { font-size: 28px; }
  .admission-price {
    font-family: "Philosopher", "Georgia", serif;
    font-weight: 700;
    font-size: 58px;
    text-shadow: 3px 4px 6px rgba(80, 60, 0, 0.45);
  }

  .showtime { font-size: 31px; }
  .showtime-fri { top: 765px; }
  .showtime-weekend { top: 808px; }

  .rule {
    position: absolute;
    left: 113px; width: 550px; height: 5px;
    background: var(--rule-blue);
  }
  .rule-top { top: 873px; }
  .rule-bottom { top: 986px; }

  .burst {
    position: absolute;
    top: 892px;
    width: 76px; height: 76px;
    border-radius: 50%;
    background: var(--burst-red);
  }
  .burst-left { left: 42px; }
  .burst-right { left: 662px; }

  .signed { font-size: 31px; }
  .signed-title { top: 892px; }
  .signed-date { top: 933px; }

  .tickets-intro { top: 1018px; font-size: 24px; }
  .tickets-site { top: 1056px; font-size: 40px; font-weight: 400; letter-spacing: 1px; }
  .tickets-phone { top: 1104px; font-size: 32px; }
  .tickets-phone strong { font-size: 36px; font-weight: 400; }
  .tickets-outro { top: 1147px; font-size: 26px; }
</style>
</head>
<body>
<main class="poster">
  <div class="backdrop-pattern" role="img" aria-label="Yellow background of overlapping concentric circle rings"></div>

  <header class="brand">
    <span class="brand-dot" aria-hidden="true"></span>
    <span class="brand-name">
      <span class="brand-initials">LFDW</span>
      <span class="brand-full">Little Footlights Drama Workshop</span>
    </span>
  </header>

  <p class="line presents">~ Presents ~</p>
  <h1 class="line title">Lanterns in Barrowmere</h1>
  <p class="line author">by Edmund Farrowby</p>
  <p class="line adapter">Adapted by Dennis Paulwick</p>
  <p class="line dates">June 8th - June 17, 2012</p>
  <p class="line venue">482 N. Larkmoor Avenue, Shepherdstown, WV</p>

  <div class="admission">
    <span class="admission-label">General Admission</span>
    <span class="admission-price">$8.00</span>
  </div>

  <p class="line showtime showtime-fri">Fridays................7:00pm</p>
  <p class="line showtime showtime-weekend">Saturdays &amp; Sundays.............2:00pm</p>

  <div class="rule rule-top"></div>
  <div class="burst burst-left" role="img" aria-label="Red starburst ornament"></div>
  <p class="line signed signed-title">Sign Interpreted Performance</p>
  <p class="line signed signed-date">Friday, June 15th, 2012</p>
  <div class="burst burst-right" role="img" aria-label="Red starburst ornament"></div>
  <div class="rule rule-bottom"></div>

  <p class="line tickets-intro">Purchase tickets online at</p>
  <p class="line tickets-site">MyLFDW.com</p>
  <p class="line tickets-phone">or call <strong>304-555-0187</strong></p>
  <p class="line tickets-outro">for more information</p>
</main>
</body>
</html>
```